THE TALL COPPER ATLAS OF PORTS

subtitle: AN INTRO TO SEARCH ENGINE OPTIMIZATION
background: white
dimensions: 1562x2500

Target Market(s)

Marketing professionals

Industry/Entity Type

Digital Marketing

Font styles to use
Sans Serif

Colors
ffffff
1b1b1b
3176b5

Requirements
Should not have
• Images or graphics

```html
<!DOCTYPE html>
<html lang="en">
<head>
<meta charset="utf-8">
<title>The Tall Copper Atlas of Ports</title>
<link rel="stylesheet" href="https://fonts.googleapis.com/css2?family=Open+Sans:wght@300;400;700;800&display=swap">
<style>
  :root {
    --paper: #ffffff;
    --ink: #1b1b1b;
    --brand-blue: #3176b5;
    --shadow: rgba(0, 0, 0, 0.55);
  }
  html, body {
    margin: 0;
    padding: 0;
    width: 750px;
    height: 1200px;
    overflow: hidden;
    background: var(--paper);
  }
  .cover {
    position: relative;
    width: 750px;
    height: 1200px;
    background: var(--paper);
    font-family: "Open Sans", Arial, sans-serif;
  }
  .title-lockup {
    position: absolute;
    left: 0;
    top: 0;
    width: 750px;
    height: 700px;
  }
  .word-the { fill: var(--brand-blue); font-weight: 800; font-size: 54px; }
  .word-tall { fill: var(--brand-blue); font-weight: 400; font-size: 54px; }
  .word-copper { fill: var(--paper); font-weight: 800; font-size: 138px; }
  .copper-band { fill: var(--brand-blue); }
  .word-atlas { fill: var(--brand-blue); font-weight: 800; font-size: 146px; }
  .word-of { fill: var(--brand-blue); font-weight: 400; font-size: 72px; }
  .ports-band { fill: var(--paper); }
  .word-ports { fill: var(--ink); font-weight: 800; font-size: 118px; }
</style>
</head>
<body>
<main class="cover">
  <svg class="title-lockup" viewBox="0 0 750 700" xmlns="http://www.w3.org/2000/svg" role="heading" aria-level="1" aria-label="The Tall Copper Atlas of Ports">
    <defs>
      <filter id="letter-shadow" x="-10%" y="-10%" width="130%" height="140%">
        <feGaussianBlur in="SourceAlpha" stdDeviation="4"/>
        <feOffset dx="4" dy="7" result="blur"/>
        <feFlood flood-color="#000" flood-opacity="0.6"/>
        <feComposite in2="blur" operator="in"/>
        <feMerge><feMergeNode/><feMergeNode in="SourceGraphic"/></feMerge>
      </filter>
      <filter id="edge-blur" x="-5%" y="-200%" width="110%" height="500%">
        <feGaussianBlur stdDeviation="3"/>
      </filter>
    </defs>

    <!-- Copper line on blue band -->
    <rect class="copper-band" x="152" y="252" width="374" height="102"/>
    <text class="word-copper" x="142" y="352" textLength="384" lengthAdjust="spacingAndGlyphs" filter="url(#letter-shadow)">COPPER</text>

    <!-- Top line, kept clear above the band -->
    <text class="word-the" x="148" y="248" textLength="104" lengthAdjust="spacingAndGlyphs">THE</text>
    <text class="word-tall" x="268" y="248" textLength="146" lengthAdjust="spacingAndGlyphs">TALL</text>

    <!-- Atlas line -->
    <text class="word-atlas" x="158" y="465" textLength="372" lengthAdjust="spacingAndGlyphs">ATLAS</text>
    <text class="word-of" x="553" y="465" textLength="58" lengthAdjust="spacingAndGlyphs">of</text>

    <!-- Ports band with soft edge shadows -->
    <rect x="170" y="484" width="432" height="6" rx="3" fill="var(--shadow)" filter="url(#edge-blur)"/>
    <rect x="170" y="592" width="432" height="7" rx="3" fill="var(--shadow)" filter="url(#edge-blur)"/>
    <rect class="ports-band" x="163" y="489" width="444" height="105"/>
    <text class="word-ports" x="385" y="587" text-anchor="middle" textLength="330" lengthAdjust="spacingAndGlyphs">PORTS</text>
  </svg>
</main>
</body>
</html>
```